Business Card Design

I need a business card design for my law office based in Pasadena, California. I am a sole practitioner and I specialize in business transaction and litigation, probate and estate planning, taxation law, corporate and business formation, immigration and real estate. I want something that is simple, yet stands out.

A friend helped to create a logo about 6 years ago. I am open to new ideas to changing the logo.

Industry/Entity Type

Business

Contact Information for Business Card

Law Offices of Dorvan L. Mabry
842 W. Larkspur Ave., Suite 319
Pasadena, CA 90287
Tel: 626-555-0174
Fax: 626-555-0139
Email: dmabry@dlmlegalgroup.example

Attorney: Dorvan L. Mabry

```html
<!DOCTYPE html>
<html lang="en">
<head>
<meta charset="utf-8">
<title>Dorvan L. Mabry — Business Card</title>
<link rel="stylesheet" href="https://fonts.googleapis.com/css2?family=Cinzel:wght@500;600&family=Tinos&family=Open+Sans:wght@400&display=swap">
<style>
  :root {
    --backdrop: #9a9b9c;
    --card-light: #ececec;
    --card-dark: #1e1e1e;
    --ink: #1f1f1f;
    --ink-soft: #555555;
    --band-grey: #8a8a8a;
    --paper-white: #f2f2f2;
  }
  * { margin: 0; padding: 0; box-sizing: border-box; }
  html, body {
    width: 1105px; height: 1200px; overflow: hidden;
    background: var(--backdrop);
  }
  .sheet { position: relative; width: 1105px; height: 1200px; }
  .card {
    position: absolute; left: 180px; width: 745px; height: 426px; overflow: hidden;
  }
  .card-front { top: 118px; background: var(--card-light); color: var(--ink); }
  .card-back { top: 636px; background: var(--card-dark); color: var(--paper-white); }

  .holder { position: absolute; left: 47px; top: 148px; }
  .holder-name {
    font-family: "Cinzel", serif; font-weight: 600; font-size: 29px; letter-spacing: 0.5px;
  }
  .holder-title {
    font-family: "Tinos", serif; font-size: 22px; color: var(--ink-soft); margin-top: 2px;
  }

  .firm-lockup {
    position: absolute; right: 40px; top: 140px; width: 280px; text-align: center;
  }
  .firm-prefix {
    font-family: "Tinos", serif; font-size: 11px; letter-spacing: 3px; text-transform: uppercase;
  }
  .firm-rule { height: 1px; background: var(--ink); margin: 5px 0 6px; }
  .firm-name {
    font-family: "Cinzel", serif; font-weight: 500; font-size: 30px; line-height: 1;
  }

  .contact-list, .address {
    position: absolute; top: 288px; list-style: none;
    font-family: "Tinos", serif; font-size: 19px; line-height: 28.5px; color: #2b2b2b;
  }
  .contact-list { left: 50px; }
  .contact-list li { display: flex; align-items: center; gap: 10px; }
  .contact-list svg { width: 16px; height: 16px; fill: var(--ink); flex: none; }
  .address { right: 47px; text-align: right; font-style: normal; }

  .footer-band {
    position: absolute; left: 0; bottom: 0; width: 100%; height: 24px; background: var(--card-dark);
  }
  .footer-band .accent {
    position: absolute; right: 0; top: 0; width: 177px; height: 100%; background: var(--band-grey);
  }
  .footer-band .accent-square {
    position: absolute; left: 8px; top: 7px; width: 10px; height: 10px; background: var(--paper-white);
  }

  .back-name {
    position: absolute; left: 0; right: 0; top: 180px; text-align: center;
    font-family: "Cinzel", serif; font-weight: 600; font-size: 46px; letter-spacing: 1px;
  }
  .website {
    position: absolute; left: 0; right: 0; top: 350px; text-align: center;
    font-family: "Open Sans", sans-serif; font-size: 18px; letter-spacing: 2.5px;
  }
</style>
</head>
<body>
<main class="sheet">
  <section class="card card-front">
    <div class="holder">
      <h1 class="holder-name">Dorvan L. Mabry</h1>
      <p class="holder-title">CEO/Founder</p>
    </div>

    <div class="firm-lockup">
      <p class="firm-prefix">Law Offices of</p>
      <div class="firm-rule"></div>
      <p class="firm-name">Dorvan L. Mabry</p>
    </div>

    <ul class="contact-list">
      <li>
        <svg viewBox="0 0 16 16" aria-hidden="true"><path d="M3.5 1l2.5 3-1.5 2c1 2 2.5 3.5 4.5 4.5l2-1.5 3 2.5-1.5 3C7 14.5 1.5 9 1 3.5z"/></svg>
        626-555-0174
      </li>
      <li>
        <svg viewBox="0 0 16 16" aria-hidden="true"><rect x="4" y="1" width="8" height="4"/><rect x="1" y="6" width="14" height="6" rx="1"/><rect x="4" y="10" width="8" height="5" fill="#ececec" stroke="#1f1f1f"/></svg>
        626-555-0139
      </li>
      <li>
        <svg viewBox="0 0 16 16" aria-hidden="true"><rect x="1" y="3" width="14" height="10"/><path d="M1 3l7 6 7-6" fill="none" stroke="#ececec" stroke-width="1.3"/></svg>
        dmabry@dlmlegalgroup.example
      </li>
    </ul>

    <address class="address">
      842 W. Larkspur Ave.<br>
      Suite 319<br>
      Pasadena, CA 90287
    </address>

    <div class="footer-band">
      <div class="accent"><span class="accent-square"></span></div>
    </div>
  </section>

  <section class="card card-back">
    <p class="back-name">Dorvan L. Mabry</p>
    <p class="website">www.dlmlegalgroup.example</p>
  </section>
</main>
</body>
</html>
```